Body therapist needs a business card

I need a card for my business which is teaching trainings in body therapy, the company is called Wexcombe Educational Group. I teach to massage therapists around Australia, South East Asia and the USA. I am attaching my logo which will guide you as to what colours I would like to have you consider. Please consult my website to find out more about what I do. www.corvantela.com.au

My name is Daniel Wexcombe. My phone number is (03) 9417 2608 or 0461753208. email is info@corvantela.com.au

```html
<!DOCTYPE html>
<html lang="en">
<head>
<meta charset="utf-8">
<title>Wexcombe Educational Group – Business Card</title>
<link href="https://fonts.googleapis.com/css2?family=Lato:wght@400;700&display=swap" rel="stylesheet">
<style>
  :root {
    --backdrop: #d6d6d6;
    --brown: #8f4e22;
    --red: #b41f24;
    --lime: #c9d92a;
    --white: #ffffff;
    --ink: #3a3a3a;
  }
  * { box-sizing: border-box; margin: 0; padding: 0; }
  html, body { width: 1000px; height: 1200px; overflow: hidden; }
  body {
    background: var(--backdrop);
    font-family: "Lato", sans-serif;
    position: relative;
  }
  .card {
    position: absolute;
    width: 778px;
    height: 446px;
    overflow: hidden;
    box-shadow: 0 6px 18px rgba(0,0,0,0.35);
  }
  .card--front { left: 111px; top: 120px; background: var(--white); }
  .card--back { left: 109px; top: 633px; background: var(--brown); }
  .card-waves { position: absolute; left: 0; top: 0; width: 100%; height: 100%; }

  .brand { position: absolute; }
  .brand-mark { position: absolute; border-radius: 50%; }
  .brand-name { position: absolute; white-space: nowrap; font-weight: 400; }

  .card--front .brand { left: 72px; top: 180px; }
  .card--front .brand-mark { left: 0; top: 4px; width: 62px; height: 62px; background: var(--brown); }
  .card--front .brand-name { left: 104px; color: var(--brown); }
  .card--front .brand-name .title { display: block; font-size: 27px; letter-spacing: 0.5px; line-height: 32px; }
  .card--front .brand-name .sub { display: block; font-size: 14px; line-height: 18px; }

  .divider { position: absolute; left: 388px; top: 116px; width: 2px; height: 216px; background: var(--red); }

  .contact { position: absolute; left: 430px; top: 110px; color: var(--ink); }
  .contact-name { font-size: 28px; font-weight: 700; line-height: 34px; color: var(--brown); }
  .contact-name .surname { color: var(--red); }
  .contact-role { font-size: 18px; line-height: 22px; margin-bottom: 14px; }
  .contact-address { font-size: 18px; line-height: 25px; margin-bottom: 12px; }
  .contact-list { list-style: none; }
  .contact-list li { display: flex; align-items: center; font-size: 18px; line-height: 25px; }
  .contact-list svg { width: 16px; height: 16px; margin-right: 10px; fill: var(--brown); }

  .card--back .brand { left: 148px; top: 150px; }
  .card--back .brand-mark { left: 0; top: 0; width: 146px; height: 146px; background: var(--white); }
  .card--back .brand-name { left: 182px; top: 28px; color: var(--white); }
  .card--back .brand-name .title { display: block; font-size: 46px; letter-spacing: 1px; line-height: 54px; }
  .card--back .brand-name .sub { display: block; font-size: 23px; line-height: 30px; }
</style>
</head>
<body>

<section class="card card--front">
  <svg class="card-waves" viewBox="0 0 778 446" preserveAspectRatio="none" aria-hidden="true">
    <path d="M0,368 Q330,440 778,420 L778,446 L0,446 Z" fill="var(--brown)"/>
    <path d="M185,406 Q520,436 778,398" fill="none" stroke="var(--white)" stroke-width="4"/>
    <path d="M185,404 Q520,432 778,364 L778,394 Q520,430 185,404 Z" fill="var(--red)"/>
  </svg>

  <div class="brand">
    <span class="brand-mark"></span>
    <span class="brand-name">
      <span class="title">Wexcombe</span>
      <span class="sub">Educational Group</span>
    </span>
  </div>

  <div class="divider"></div>

  <div class="contact">
    <p class="contact-name">Daniel <span class="surname">Wexcombe</span></p>
    <p class="contact-role">Owner</p>
    <p class="contact-address">P.O. Box 2074, Ferndale North<br>Victoria, 3145, Australia</p>
    <ul class="contact-list">
      <li><svg viewBox="0 0 24 24"><path d="M6.6 10.8a15.1 15.1 0 0 0 6.6 6.6l2.2-2.2a1 1 0 0 1 1-.25 11.4 11.4 0 0 0 3.6.57 1 1 0 0 1 1 1V20a1 1 0 0 1-1 1A17 17 0 0 1 3 4a1 1 0 0 1 1-1h3.5a1 1 0 0 1 1 1c0 1.25.2 2.45.57 3.57a1 1 0 0 1-.25 1z"/></svg>(03) 9417 2608</li>
      <li><svg viewBox="0 0 24 24"><path d="M7 1h10a2 2 0 0 1 2 2v18a2 2 0 0 1-2 2H7a2 2 0 0 1-2-2V3a2 2 0 0 1 2-2zm0 3v15h10V4zm5 16.2a1 1 0 1 0 0 .01z"/></svg>0461753208</li>
      <li><svg viewBox="0 0 24 24"><path d="M2 5h20v14H2zm2 2v.5l8 5 8-5V7zm0 3v7h16v-7l-8 5z"/></svg>info@corvantela.com.au</li>
      <li><svg viewBox="0 0 24 24"><path d="M12 2a10 10 0 1 0 0 20 10 10 0 0 0 0-20zm6.9 6h-3a15 15 0 0 0-1.3-3.9A8 8 0 0 1 18.9 8zM12 4c.9 1.2 1.6 2.5 2 4h-4c.4-1.5 1.1-2.8 2-4zM4.3 14a8 8 0 0 1 0-4h3.4a16 16 0 0 0 0 4zm.8 2h3a15 15 0 0 0 1.3 3.9A8 8 0 0 1 5.1 16zm3-8h-3a8 8 0 0 1 4.3-3.9A15 15 0 0 0 8.1 8zM12 20c-.9-1.2-1.6-2.5-2-4h4c-.4 1.5-1.1 2.8-2 4zm2.3-6H9.7a14 14 0 0 1 0-4h4.6a14 14 0 0 1 0 4zm.3 5.9a15 15 0 0 0 1.3-3.9h3a8 8 0 0 1-4.3 3.9zm1.7-5.9a16 16 0 0 0 0-4h3.4a8 8 0 0 1 0 4z"/></svg>www.corvantela.com.au</li>
    </ul>
  </div>
</section>

<section class="card card--back">
  <svg class="card-waves" viewBox="0 0 782 446" preserveAspectRatio="none" aria-hidden="true">
    <path d="M0,367 Q360,430 782,400 L782,446 L0,446 Z" fill="var(--lime)"/>
    <path d="M200,405 Q540,432 782,364 L782,400 Q540,428 200,405 Z" fill="var(--red)"/>
  </svg>

  <div class="brand">
    <span class="brand-mark"></span>
    <span class="brand-name">
      <span class="title">Wexcombe</span>
      <span class="sub">Educational Group</span>
    </span>
  </div>
</section>

</body>
</html>
```